Self-Publisher seeking a professional Book Cover design

Paperback novel, science-fiction/mind-fiction. Title “Tovald’s Hollow”. Will be published via Pellow PBX and must meet their sizing requirements for a Book Cover (‘the spine”). (The book is 362 pages). The overall concept of design should be relatively simple, playing with themes of dark/blackness/space/unconscious/insanity-themes. Initially I had in mind a dark cover with something floating small and distant in the darkness like a sort of “space-cocoon”/hibernation-tank for an astronaut. (just something to get started thinking with). I am very open to any concepts.

From the back cover:
“In the year 3438, a discovery of a lifetime is made, and promises new light for a whole new generation of mankind which has permanently stagnated, becoming little more than slaves to their own technology which itself has already plateaued. Life goes on, yet for man, it stopped over a millennia ago. A secret project begun in the Ancient-American West in the year 1947, has catastrophic implications for the modern people’s of 3438. A discovery in space that lay apparently dormant for over a thousand years, mysteriously hidden from mankind’s ever evolving technological grasp, leads to a culture-shattering revelation that can only have one outcome. Chaos. …”

Target Market(s)

25-45 yr.

Industry/Entity Type

science-fiction, mind-bending, esotericism, psychological, space,

Font styles to use
Serif

Colors

Designer to choose colors to be used in the design.

Requirements
Must have
• darkness, with perhaps elements of bright light???
Should not have
• nothing too colorful. think, “unconscious”.

```html
<!DOCTYPE html>
<html lang="en">
<head>
<meta charset="utf-8">
<title>Tovald’s Hollow — Full Cover</title>
<link rel="stylesheet" href="https://fonts.googleapis.com/css2?family=Jura:wght@400;500;600;700&display=swap">
<style>
  :root {
    --space-black: #05060c;
    --space-deep: #0b0d1a;
    --nebula-dust: #2a2633;
    --tunnel-blue: #7fb4e0;
    --tunnel-core: #cfe6f7;
    --ink-white: #f4f6f8;
    --title-glow: rgba(190, 205, 225, 0.55);
    --spine-band: #000000;
  }
  * { margin: 0; padding: 0; box-sizing: border-box; }
  html, body {
    width: 1200px; height: 844px; overflow: hidden;
    background: var(--space-black);
  }
  .cover {
    position: relative; width: 1200px; height: 844px; overflow: hidden;
    font-family: "Jura", sans-serif; color: var(--ink-white);
  }
  .starfield {
    position: absolute; inset: 0;
    background:
      radial-gradient(ellipse 420px 160px at 260px 720px, rgba(120,110,130,0.35), transparent 70%),
      radial-gradient(ellipse 300px 120px at 560px 800px, rgba(110,100,120,0.3), transparent 70%),
      linear-gradient(180deg, var(--space-black) 0%, var(--space-deep) 60%, var(--nebula-dust) 100%);
  }
  .tunnel-art {
    position: absolute; left: 640px; top: 0; width: 560px; height: 844px;
    background:
      radial-gradient(circle at 280px 380px, var(--tunnel-core) 0%, var(--tunnel-blue) 9%, rgba(60,100,150,0.55) 22%, rgba(70,80,100,0.35) 40%, transparent 68%),
      radial-gradient(ellipse 160px 240px at 480px 470px, rgba(200,170,130,0.3), transparent 70%),
      radial-gradient(ellipse 140px 200px at 170px 450px, rgba(190,160,120,0.22), transparent 70%);
  }
  .title {
    position: absolute; text-align: center; font-weight: 600; line-height: 1;
    text-transform: uppercase; color: var(--ink-white);
    text-shadow: 0 0 2px #000, 0 0 6px var(--title-glow), 2px 3px 4px rgba(0,0,0,0.9);
  }
  .title span { display: block; }
  .back-title { left: 100px; top: 80px; width: 352px; }
  .back-title .line-1 { font-size: 62px; letter-spacing: 2px; }
  .back-title .line-2 { font-size: 80px; margin-top: 12px; letter-spacing: 1px; }
  .front-title { left: 700px; top: 104px; width: 460px; }
  .front-title .line-1 { font-size: 78px; letter-spacing: 3px; }
  .front-title .line-2 { font-size: 104px; margin-top: 14px; letter-spacing: 2px; }
  .blurb {
    position: absolute; left: 30px; top: 262px; width: 504px;
    text-align: center; font-size: 12.2px; line-height: 16.8px; letter-spacing: 0.4px;
    text-shadow: 0 0 3px #000;
  }
  .blurb p + p { margin-top: 16.8px; }
  .spine-band {
    position: absolute; left: 570px; top: 76px; width: 58px; height: 496px;
    background: var(--spine-band); border-radius: 14px;
  }
  .spine-title {
    position: absolute; left: 599px; top: 80px;
    writing-mode: vertical-rl; font-weight: 600; font-size: 52px; letter-spacing: 2px;
    line-height: 1; text-transform: uppercase; transform: translateX(-50%);
    text-shadow: 0 0 5px var(--title-glow);
  }
  .spine-author {
    position: absolute; left: 598px; top: 612px;
    writing-mode: vertical-rl; font-size: 20px; font-weight: 500; transform: translateX(-50%);
  }
  .front-author {
    position: absolute; left: 700px; top: 772px; width: 460px; text-align: center;
    font-size: 31px; font-weight: 500; letter-spacing: 6px; text-transform: uppercase;
  }
</style>
</head>
<body>
  <main class="cover">
    <div class="starfield" role="img" aria-label="Deep starfield with faint milky way across the lower back cover"></div>
    <div class="tunnel-art" role="img" aria-label="Wireframe space tunnel glowing blue at its core, with shattered glass shards bursting toward the viewer"></div>

    <section class="back-cover">
      <h2 class="title back-title"><span class="line-1">Tovald’s</span><span class="line-2">Hollow</span></h2>
      <div class="blurb">
        <p>In the year 3438, a discovery of a lifetime is made, and promises new light for a whole new generation of mankind which has permanently stagnated, becoming little more than slaves to their own technology which itself has already plateaued.<br>Life goes on, yet for man, it stopped over a millennia ago.</p>
        <p>A secret project begun in the Ancient-American West in the year 1947, has catastrophic implications for the modern people’s of 3438.</p>
        <p>A discovery in space that lay apparently dormant for over a thousand years, mysteriously hidden from mankind’s ever evolving technological grasp, leads to a culture-shattering revelation that can only have one outcome.<br>Chaos. …”</p>
      </div>
    </section>

    <section class="spine">
      <div class="spine-band"></div>
      <div class="spine-title">Tovald’s Hollow</div>
      <div class="spine-author">Authors Name</div>
    </section>

    <section class="front-cover">
      <h1 class="title front-title"><span class="line-1">Tovald’s</span><span class="line-2">Hollow</span></h1>
      <div class="front-author">Authors Name</div>
    </section>
  </main>
</body>
</html>
```